Website for QuillbrookCrew presentation

We need a new website, ideally as a wordpress there, for QuillbrookCrew - we focus on machine learning, big data, data science and data analytics. This website should have two main sections - team presentation, introduction and offered services as static pages, and a blog section.

Target Market(s)

Companies which would like to hire the consultants for data science

Industry/Entity Type

Data Service

Font styles to use
Sans Serif

Colors

Designer to choose colors to be used in the design.

Requirements
Must have
• Wordpress template, blog and presentation pages, nice background images, incorporate the existing logo from brief
Nice to have
• match the word and ppt existing templates for quillbrook crew

```html
<!DOCTYPE html>
<html lang="en">
<head>
<meta charset="utf-8">
<title>QuillbrookCrew</title>
<link href="https://fonts.googleapis.com/css2?family=Lato:wght@400;700;900&family=Roboto:wght@400;700&display=swap" rel="stylesheet">
<style>
:root{
  --blue:#1a87c4;
  --blue-dark:#1577ad;
  --ink:#555b61;
  --text:#666c72;
  --pale:#e6f1f9;
  --footer:#e4eff8;
  --white:#ffffff;
}
*{margin:0;padding:0;box-sizing:border-box}
html,body{width:1200px;height:2679px;overflow:hidden;background:var(--white)}
body{position:relative;font-family:"Lato",sans-serif;color:var(--text)}
.abs{position:absolute}
.brand{display:flex;align-items:center;gap:10px;font-family:"Lato",sans-serif;font-weight:900;color:var(--blue);font-size:20px;line-height:1.05}
.brand .dot{width:26px;height:26px;border-radius:50%;background:var(--blue)}
.nav a{position:absolute;top:40px;font-size:16px;color:var(--ink);text-decoration:none}
.nav a.active{color:var(--blue)}
.btn{position:absolute;display:flex;align-items:center;justify-content:center;background:var(--blue);color:var(--white);font-weight:700;border-radius:5px;text-transform:uppercase}
.hero-title{left:80px;top:250px;font-family:"Roboto",sans-serif;font-size:46px;line-height:52px;font-weight:700;color:var(--blue)}
.hero-title span{display:block;font-weight:400;color:var(--ink)}
.hero-text{left:80px;top:375px;width:320px;font-size:15px;line-height:26px}
.section-title{left:0;width:1200px;text-align:center;font-family:"Roboto",sans-serif;font-size:37px;font-weight:400;color:var(--ink)}
.section-title b{color:var(--blue);font-weight:700}
.service{position:absolute;top:846px;width:240px;text-align:center}
.service .icon{width:84px;height:84px;border-radius:50%;background:var(--pale);margin:0 auto 30px;display:flex;align-items:center;justify-content:center}
.service h3{font-size:19px;color:var(--blue);font-weight:700;margin-bottom:6px}
.service p{font-size:15px;line-height:26px;width:215px;margin:0 auto}
.about-title{left:670px;top:1110px;font-family:"Roboto",sans-serif;font-size:37px;line-height:48px;font-weight:400;color:var(--ink)}
.about-title b{color:var(--blue);font-weight:700}
.about-text{left:670px;top:1224px;width:445px;font-size:15.5px;line-height:26px}
.card{position:absolute;top:1709px;width:323px;height:364px;border-radius:6px;overflow:hidden}
.card.photo{color:var(--white);text-align:center}
.card.photo .caption{position:absolute;left:0;right:0;top:180px;font-weight:700;font-size:16px;line-height:28px;padding:0 24px}
.card.photo .admin{position:absolute;left:0;right:0;top:256px;font-size:14px}
.avatar{position:absolute;left:50%;width:42px;height:42px;margin-left:-21px;border-radius:50%;border:2px solid var(--white)}
.card.quote{background:var(--white);box-shadow:0 4px 18px rgba(0,0,0,.12);text-align:center}
.card.quote p{position:absolute;left:0;right:0;top:38px;font-size:14.5px;line-height:26px;color:var(--ink);white-space:nowrap}
.card.quote .admin{position:absolute;left:0;right:0;top:216px;color:var(--blue);font-weight:700;font-size:14px}
.arrow{position:absolute;top:1871px;width:40px;height:40px;border-radius:50%;background:var(--pale);display:flex;align-items:center;justify-content:center}
.field{position:absolute;top:2261px;height:52px;background:var(--white);border-radius:4px;box-shadow:0 2px 10px rgba(0,0,0,.08);font-size:15px;color:var(--ink);padding:16px 14px}
.footer{left:0;top:2377px;width:1200px;height:302px;background:var(--footer)}
.fcol{position:absolute;top:2408px}
.fcol h4{font-size:16px;color:var(--blue);font-weight:700;margin-bottom:16px}
.fcol li{list-style:none;font-size:15px;line-height:31px;color:var(--ink)}
.contact-row{position:absolute;left:620px;display:flex;gap:22px;font-size:15px;line-height:26px;color:var(--ink)}
.contact-row svg{flex:none;margin-top:4px}
.social{position:absolute;top:2543px;width:14px;height:14px;border-radius:50%;background:var(--blue)}
.rule{position:absolute;height:1px;background:var(--blue)}
.copy{left:0;top:2634px;width:1200px;text-align:center;font-size:15px;color:var(--ink)}
.copy b{color:var(--blue)}
</style>
</head>
<body>

<header>
  <div class="brand abs" style="left:79px;top:30px"><span class="dot"></span><span>QUILLBROOK<br>CREW</span></div>
  <nav class="nav">
    <a class="active" style="left:495px">Home</a>
    <a style="left:595px">About</a>
    <a style="left:695px">Services</a>
    <a style="left:809px">Blog</a>
    <a style="left:900px">Contact</a>
  </nav>
  <div class="btn" style="left:1007px;top:32px;width:115px;height:39px;font-size:13px">Get started</div>
</header>

<section class="hero">
  <svg class="abs" style="left:0;top:0" width="1200" height="760" aria-hidden="true">
    <path d="M430 300 C470 220 600 200 700 240 L930 520 C990 620 960 740 860 742 C700 748 560 700 470 600 C400 520 390 380 430 300 Z" fill="#e6f1f9"/>
  </svg>
  <svg class="abs" style="left:0;top:0" width="1200" height="760" role="img" aria-label="Team working around a desk with laptops, notebooks and a plant, seen from above">
    <defs><linearGradient id="heroPhoto" x1="0" y1="0" x2="1" y2="1"><stop offset="0" stop-color="#b9a597"/><stop offset=".5" stop-color="#e7e4e0"/><stop offset="1" stop-color="#c9ccd0"/></linearGradient></defs>
    <path d="M768 104 H1200 V340 L900 630 C850 680 780 680 730 650 L620 560 C560 500 560 420 600 370 Z" fill="url(#heroPhoto)"/>
  </svg>
  <h1 class="hero-title abs">QUILLBROOK<span>CREW</span></h1>
  <p class="hero-text abs">Lorem Ipsum is simply dummy text of the printing&nbsp; typesetting industry. Lorem Ipsum</p>
  <div class="btn" style="left:77px;top:454px;width:146px;height:51px;font-size:16px">Contact us</div>
</section>

<section class="services">
  <h2 class="section-title abs" style="top:764px"><b>OUR</b> SERVICES</h2>
  <div class="service" style="left:73px">
    <div class="icon"><svg width="40" height="40" viewBox="0 0 40 40" fill="none" stroke="#1a87c4" stroke-width="2"><ellipse cx="20" cy="20" rx="15" ry="11"/><path d="M20 9v22M12 14c3 2 3 6 0 8M28 14c-3 2-3 6 0 8M10 26l-3 6"/></svg></div>
    <h3>Machine learning</h3><p>Lorem Ipsum is simply dummy text typesetting industry.</p>
  </div>
  <div class="service" style="left:343px">
    <div class="icon"><svg width="40" height="40" viewBox="0 0 40 40" fill="none" stroke="#1a87c4" stroke-width="2"><path d="M11 26a7 7 0 0 1 1-14 9 9 0 0 1 17 2 6 6 0 0 1 0 12Z"/><path d="M20 18v14M14 22v10M26 22v10"/></svg></div>
    <h3>Big data</h3><p>Lorem Ipsum is simply dummy text typesetting industry.</p>
  </div>
  <div class="service" style="left:614px">
    <div class="icon"><svg width="40" height="40" viewBox="0 0 40 40" fill="none" stroke="#1a87c4" stroke-width="2"><circle cx="20" cy="20" r="14"/><circle cx="20" cy="20" r="7"/><path d="M20 6v7M20 27v7M6 20h7M27 20h7"/></svg></div>
    <h3>Data science</h3><p>Lorem Ipsum is simply dummy text typesetting industry.</p>
  </div>
  <div class="service" style="left:884px">
    <div class="icon"><svg width="40" height="40" viewBox="0 0 40 40" fill="none" stroke="#1a87c4" stroke-width="2.4"><circle cx="17" cy="17" r="10"/><path d="M24 24l9 9M13 20v-3M17 20v-6M21 20v-4"/></svg></div>
    <h3>Data analytics</h3><p>Lorem Ipsum is simply dummy text typesetting industry.</p>
  </div>
</section>

<section class="about">
  <svg class="abs" style="left:0;top:1093px" width="640" height="530" aria-hidden="true">
    <path d="M250 140 C330 90 470 80 560 140 C640 200 620 330 520 430 C440 510 300 530 200 500 C150 480 150 420 170 340 C185 260 200 180 250 140 Z" fill="#e6f1f9"/>
  </svg>
  <svg class="abs" style="left:0;top:1093px" width="640" height="530" role="img" aria-label="Colleagues in a bright office meeting around a wooden table with laptops">
    <defs><linearGradient id="aboutPhoto" x1="0" y1="0" x2="1" y2="1"><stop offset="0" stop-color="#d8dcd7"/><stop offset=".55" stop-color="#c7a987"/><stop offset="1" stop-color="#9aa4ad"/></linearGradient></defs>
    <path d="M0 0 H322 L500 190 C560 255 540 340 480 400 L420 460 C390 490 350 500 310 495 H0 Z" fill="url(#aboutPhoto)"/>
  </svg>
  <h2 class="about-title abs"><b>ABOUT</b> QUILLBROOK<br>CREW</h2>
  <p class="about-text abs">Lorem Ipsum is simply dummy text of the printing and typesetting industry. Lorem Ipsum has been the industry's standard dummy text ever since the 1500s, when an unknown printer took a galley of type and scrambled it to make a type specimen book. It has survived not only five centuries, but also the leap into electronic typesetting, remaining essentially unchanged. It was popularised in the 1960s with the release of Letraset sheets containing Lorem Ipsum passages,</p>
  <div class="btn" style="left:666px;top:1470px;width:147px;height:50px;font-size:16px">Read more</div>
</section>

<section class="blog">
  <h2 class="section-title abs" style="top:1632px"><b>LATEST</b> BLOG</h2>
  <div class="arrow" style="left:18px"><svg width="18" height="18" viewBox="0 0 18 18" fill="none" stroke="#1a87c4" stroke-width="2"><path d="M15 9H3M8 4L3 9l5 5"/></svg></div>
  <div class="arrow" style="left:1141px"><svg width="18" height="18" viewBox="0 0 18 18" fill="none" stroke="#1a87c4" stroke-width="2"><path d="M3 9h12M10 4l5 5-5 5"/></svg></div>

  <article class="card photo" style="left:77px;background:linear-gradient(180deg,#dcdcdc 0%,#a8a8a8 55%,#3e3e3e 100%)" role="img" aria-label="Blog cover photo of a woman reading a document">
    <div class="caption">Lorem Ipsum is simply dummy text of the printing</div>
    <div class="admin">- Admin Name</div>
    <div class="avatar" style="top:290px;background:#c9ccd1"></div>
  </article>

  <article class="card quote" style="left:439px">
    <p>Lorem Ipsum is simply dummy text of the<br>printing and typesetting industry. Lorem<br>Ipsum has been the industry's standard<br>dummy text ever since the 1500s, when<br>an unknown printer took a galley of type<br>and scrambled specimen book.</p>
    <div class="admin">- Admin Name</div>
    <div class="avatar" style="top:248px;border:0;background:#7b8896" role="img" aria-label="Author portrait"></div>
    <div class="btn" style="left:110px;top:303px;width:103px;height:36px;font-size:13px;border-radius:4px">Read more</div>
  </article>

  <article class="card photo" style="left:800px;background:linear-gradient(180deg,#b7bcc0 0%,#7b8086 55%,#2f3235 100%)" role="img" aria-label="Blog cover photo of a team meeting in an office">
    <div class="caption">Lorem Ipsum is simply dummy text of the printing</div>
    <div class="admin">- Admin Name</div>
    <div class="avatar" style="top:290px;background:#c9ccd1"></div>
  </article>
</section>

<section class="newsletter">
  <h2 class="section-title abs" style="top:2132px"><b>NEWS</b>LETTER</h2>
  <p class="abs" style="left:0;top:2208px;width:1200px;text-align:center;font-size:15px;color:var(--ink)">For latest news or updates subscribe our newsletter</p>
  <div class="field" style="left:257px;width:291px">Enter Name*</div>
  <div class="field" style="left:559px;width:291px">Enter E-mail*</div>
  <div class="btn" style="left:861px;top:2261px;width:103px;height:52px;font-size:16px">Sign up</div>
</section>

<footer>
  <div class="footer abs"></div>
  <div class="fcol" style="left:80px"><h4>SITE MAP</h4><ul><li>Home</li><li>About</li><li>Services</li><li>Blog</li><li>Contact</li></ul></div>
  <div class="fcol" style="left:350px"><h4>SERVICES</h4><ul><li>Machine learning</li><li>Big data</li><li>Data science</li><li>Data analytics</li></ul></div>
  <div class="fcol" style="left:620px"><h4>GET IN TOUCH</h4></div>
  <div class="contact-row" style="top:2444px"><svg width="16" height="18" viewBox="0 0 16 18"><path d="M8 0a7 7 0 0 1 7 7c0 5-7 11-7 11S1 12 1 7a7 7 0 0 1 7-7z" fill="#1a87c4"/><circle cx="8" cy="7" r="2.6" fill="#e4eff8"/></svg><span style="width:200px">123, Lorem ipsum is simply dummy text of the</span></div>
  <div class="contact-row" style="top:2516px"><svg width="18" height="18" viewBox="0 0 18 18"><path d="M4 1l3 4-2 2c1 3 3 5 6 6l2-2 4 3-2 3C8 17 1 10 1 3z" fill="#1a87c4"/></svg><span>123 456 7890</span></div>
  <div class="contact-row" style="top:2570px"><svg width="18" height="14" viewBox="0 0 18 14"><rect x="0" y="1" width="18" height="12" rx="1.5" fill="#1a87c4"/><path d="M1 2l8 6 8-6" fill="none" stroke="#e4eff8" stroke-width="1.5"/></svg><span>info@quillbrookcrew.com</span></div>
  <div class="brand abs" style="left:946px;top:2446px"><span class="dot"></span><span>QUILLBROOK<br>CREW</span></div>
  <div class="rule" style="left:888px;top:2511px;width:234px"></div>
  <span class="social" style="left:954px"></span>
  <span class="social" style="left:998px"></span>
  <span class="social" style="left:1043px"></span>
  <div class="rule" style="left:77px;top:2616px;width:1046px"></div>
  <p class="copy abs">© <b>QUILLBROOK CREW</b> - 2018. All Rights Reserved.</p>
</footer>

</body>
</html>
```